Fully Functional Wix Website, Not Just Images

Please read all instructions carefully. This is NOT merely a design project where the artist will deliver static images. This project requires that the designer build a fully functional SEO optimized website within Wix then transfer full ownership to me. See attached "instructions for design" file. I have wix for other websites. Only wix is acceptable. Do not submit more than 1 design per designer. If you submit more than 1 design I will award to someone else.

Target Market(s)

see attachments and brisvale482.com

Industry/Entity Type

Coding

Coded - Design and coding required

Number of Pages Required

4 page

Font styles to use
Other font styles liked:
• see attachments and brisvale482.com

Requirements
Must have
Nice to have
Should not have

```html
<!DOCTYPE html>
<html lang="en">
<head>
<meta charset="utf-8">
<title>Captain Harlan's Boat Training & Charters</title>
<link rel="stylesheet" href="https://fonts.googleapis.com/css2?family=Cinzel:wght@500;600&family=Raleway:ital,wght@0,400;0,500;0,600;0,700;1,400&display=swap">
<style>
:root{
  --gold:#c9a21c;
  --gold-band:#cba51f;
  --ink:#161616;
  --text:#333;
  --navy:#142338;
  --soft:#f4f4f4;
  --footer:#0b0b0b;
  --white:#fff;
}
*{margin:0;padding:0;box-sizing:border-box}
html,body{width:1200px;height:3705px;overflow:hidden;background:var(--white)}
body{position:relative;font-family:'Raleway',sans-serif;color:var(--text)}
.abs{position:absolute}
.serif{font-family:'Cinzel',serif;font-weight:500;color:var(--ink);letter-spacing:1px}
.btn{position:absolute;border:2px solid var(--gold);color:var(--gold);font-weight:600;font-size:14px;display:flex;align-items:center;justify-content:center;text-transform:uppercase;text-decoration:none;background:transparent}
.center{text-align:center;left:0;width:1200px}

/* header */
.site-header{top:0;left:0;width:1200px;height:137px;background:var(--white)}
.brand-bump{left:90px;top:-10px;width:192px;height:192px;border-radius:50%;background:var(--white);display:flex;align-items:center;justify-content:center;z-index:3}
.brand-name{width:130px;text-align:center;font-weight:700;font-size:15px;line-height:1.25;color:var(--navy)}
.nav a{position:absolute;top:64px;font-size:15px;font-weight:600;color:var(--ink);text-decoration:none}
.nav a.active{color:var(--gold)}

/* hero */
.hero{top:137px;left:0;width:1200px;height:600px;background:linear-gradient(180deg,#6f8fb4 0%,#9db5cd 38%,#4d6f8c 52%,#7d8c96 75%,#3e4a57 100%)}
.hero-shade{top:137px;left:0;width:1200px;height:600px;background:linear-gradient(90deg,rgba(20,25,30,.55) 0%,rgba(20,25,30,.15) 40%,rgba(20,25,30,.1) 100%)}
.hero-title{top:340px;font-size:41px;color:var(--white)}
.hero-text{top:403px;left:200px;width:800px;text-align:center;color:var(--white);font-size:21px;line-height:31px;font-weight:500}

/* series */
.section-title{font-size:41px}
.book{top:971px;width:295px;height:380px;border:2px solid var(--navy)}
.book-a{left:127px;background:linear-gradient(180deg,#223c70 0%,#4a6fa2 40%,#d99a3c 62%,#2d3f5c 85%,#122038 100%)}
.book-b{left:453px;background:linear-gradient(180deg,#1d3463 0%,#4b79b8 45%,#2f5f94 65%,#1d3460 85%,#0f1d36 100%)}
.book-c{left:778px;background:linear-gradient(180deg,#1f3a6d 0%,#5d8fcd 42%,#9fb9d6 58%,#3d6ea6 78%,#102039 100%)}

/* about */
.about{top:1594px;left:0;width:1200px;height:762px;background:var(--soft)}
.about-text{font-size:15.5px;line-height:25px;text-align:justify}
.portrait{left:112px;top:1750px;width:484px;height:484px;border-radius:50%;border:14px solid var(--gold);background:var(--soft);padding:14px}
.portrait-photo{width:100%;height:100%;border-radius:50%;background:linear-gradient(180deg,#e2e2e2,#cfd2d6)}
.creds{top:1978px;left:650px;width:440px;list-style:none}
.creds li{position:absolute;left:0;display:flex;align-items:center;gap:24px;font-size:15px;font-weight:500;color:var(--ink);line-height:22px}
.creds svg{width:34px;height:34px;flex:none}

/* reviews */
.reviews{top:2356px;left:0;width:1200px;height:431px;background:var(--gold-band)}

/* services */
.service{top:2988px;width:230px;text-align:center}
.service h3{font-size:16px;font-weight:700;color:var(--ink);margin-top:30px;letter-spacing:.3px}
.service p{font-size:18px;line-height:26px;margin-top:14px;color:#444}

/* footer */
.site-footer{top:3387px;left:0;width:1200px;height:318px;background:var(--footer);color:var(--white)}
.site-footer h4{position:absolute;top:64px;font-size:18px;font-weight:700;color:var(--gold)}
.site-footer .col a,.site-footer .col span{display:block;font-size:16px;font-weight:500;color:var(--white);text-decoration:none;height:30px}
.social{left:813px;top:100px;display:flex;gap:14px}
.social a{display:block;width:18px;height:18px}
.social svg{width:18px;height:18px;display:block}
</style>
</head>
<body>

<header class="site-header abs">
  <div class="brand-bump abs"><div class="brand-name">Captain Harlan's Boat Training &amp; Charters</div></div>
  <nav class="nav">
    <a class="active" href="#" style="left:352px">HOME</a>
    <a href="#" style="left:432px">SERVICES</a>
    <a href="#" style="left:540px">BOATING AIDS</a>
    <a href="#" style="left:683px">GALLERY</a>
    <a href="#" style="left:787px">CONTACT</a>
  </nav>
  <a class="btn" href="#" style="left:902px;top:50px;width:186px;height:46px">Book a Charter</a>
</header>

<section>
  <div class="hero abs" role="img" aria-label="Photo of a captain at the helm of a boat on open water"></div>
  <div class="hero-shade abs"></div>
  <h1 class="serif hero-title abs center">CONFIDENCE AT THE HELM</h1>
  <p class="hero-text abs">Whether you’re new to boating or ready for your next adventure, Captain Harlan’s Boat Training &amp; Charters, LLC helps you build skills, make memories, and explore with confidence.</p>
  <a class="btn" href="#" style="left:492px;top:519px;width:216px;height:46px">View Boat Training</a>
</section>

<section>
  <h2 class="serif section-title abs center" style="top:836px">THE FIRST MATE SERIES</h2>
  <p class="abs center" style="top:903px;font-size:21px;font-weight:500;color:var(--ink)">Practical guidance. Real-world insights. A safer, smarter you.</p>
  <div class="book book-a abs" role="img" aria-label="Book cover: guide to buying a boat, by Captain Harlan T. Wexley"></div>
  <div class="book book-b abs" role="img" aria-label="Book cover: guide to storage, maintenance and safety on the water, by Captain Harlan T. Wexley"></div>
  <div class="book book-c abs" role="img" aria-label="Book cover: guide to planning great boating trips, by Captain Harlan T. Wexley"></div>
  <a class="btn" href="#" style="left:412px;top:1403px;width:377px;height:45px">View the First Mate Series on the Bookstore</a>
  <p class="abs center" style="top:1477px;font-size:19px;font-style:italic;color:var(--ink)">Visit Captain Harlan’s Online Author Page</p>
</section>

<section>
  <div class="about abs"></div>
  <div class="portrait abs"><div class="portrait-photo" role="img" aria-label="Portrait photo of Captain Harlan"></div></div>
  <h2 class="serif abs" style="top:1652px;left:650px;font-size:43px">ABOUT ME</h2>
  <p class="about-text abs" style="top:1726px;left:650px;width:440px">I’m Captain Harlan — a U.S. Coast Guard licensed captain, certified boating instructor, and author of the First Mate Series.</p>
  <p class="about-text abs" style="top:1813px;left:650px;width:440px">With years of hands-on experience on the water, I’m passionate about helping others build the confidence and skills they need to boat safely and enjoyably. Whether you’re training, chartering, or just looking for trusted guidance, I’m here to help you make the most of your time on the water.</p>
  <ul class="creds abs">
    <li style="top:0"><svg viewBox="0 0 34 34"><g fill="none" stroke="var(--gold)" stroke-width="3" stroke-linecap="round"><circle cx="17" cy="6" r="3"/><line x1="17" y1="9" x2="17" y2="30"/><line x1="10" y1="14" x2="24" y2="14"/><path d="M5 20 Q8 30 17 30 Q26 30 29 20"/></g></svg><span>U.S. Coast Guard Licensed Captain (Master,<br>Near Coastal)</span></li>
    <li style="top:70px"><svg viewBox="0 0 34 34"><path d="M17 2 L30 7 V16 C30 24 24 30 17 32 C10 30 4 24 4 16 V7 Z" fill="var(--gold)"/><path d="M11 17 L15 21 L23 12" fill="none" stroke="#fff" stroke-width="3"/></svg><span>Certified Boating Instructor</span></li>
    <li style="top:121px"><svg viewBox="0 0 34 34"><path d="M8 4 H30 L26 28 H4 Z" fill="var(--gold)"/><path d="M4 28 L4 31 H25" fill="none" stroke="var(--gold)" stroke-width="2.5"/><line x1="11" y1="10" x2="24" y2="10" stroke="#fff" stroke-width="2"/></svg><span>Published Author – The First Mate Series</span></li>
    <li style="top:172px"><svg viewBox="0 0 34 34"><circle cx="17" cy="17" r="12" fill="none" stroke="var(--gold)" stroke-width="6"/><circle cx="17" cy="17" r="12" fill="none" stroke="#fff" stroke-width="6" stroke-dasharray="5 14"/></svg><span>Years of Real-World Charter Experience</span></li>
    <li style="top:223px"><svg viewBox="0 0 34 34"><g stroke="var(--gold)" stroke-width="2.5" fill="none"><circle cx="17" cy="17" r="10"/><circle cx="17" cy="17" r="3"/><line x1="17" y1="2" x2="17" y2="32"/><line x1="2" y1="17" x2="32" y2="17"/><line x1="6" y1="6" x2="28" y2="28"/><line x1="28" y1="6" x2="6" y2="28"/></g></svg><span>Committed to Safer, More Confident Boaters</span></li>
  </ul>
  <a class="btn" href="#" style="left:650px;top:2269px;width:153px;height:48px">Learn More</a>
</section>

<section>
  <div class="reviews abs"></div>
  <h2 class="serif abs center" style="top:2422px;font-size:43px;color:var(--white)">CLIENT REVIEWS</h2>
  <p class="abs" style="top:2492px;left:220px;width:760px;text-align:center;color:var(--white);font-size:18px;line-height:28px;font-weight:500">“Captain Harlan is an outstanding instructor! Patient, knowledgeable, and made learning to boat fun and stress-free.”</p>
  <svg class="abs" style="left:108px;top:2542px" width="40" height="60" viewBox="0 0 40 60"><path d="M32 4 L8 30 L32 56" fill="none" stroke="#fff" stroke-width="4"/></svg>
  <svg class="abs" style="left:1052px;top:2542px" width="40" height="60" viewBox="0 0 40 60"><path d="M8 4 L32 30 L8 56" fill="none" stroke="#fff" stroke-width="4"/></svg>
  <div class="abs" style="left:563px;top:2562px;width:74px;height:74px;border-radius:50%;background:linear-gradient(180deg,#8fb0cf,#c9d4dc)" role="img" aria-label="Reviewer photo"></div>
  <p class="abs center" style="top:2654px;font-size:20px;font-weight:700;color:var(--white)">— DANA W.</p>
  <p class="abs center" style="top:2684px;font-size:14px;letter-spacing:3px;color:var(--white)">★★★★★</p>
  <svg class="abs" style="left:574px;top:2724px" width="52" height="14" viewBox="0 0 52 14"><circle cx="8" cy="7" r="4" fill="none" stroke="#fff" stroke-width="1.5"/><circle cx="26" cy="7" r="4.5" fill="#fff"/><circle cx="44" cy="7" r="4.5" fill="#fff"/></svg>
</section>

<section>
  <h2 class="serif section-title abs center" style="top:2885px">OUR SERVICES</h2>
  <div class="service abs" style="left:104px">
    <svg width="60" height="64" viewBox="0 0 60 64"><g fill="var(--gold)"><circle cx="30" cy="20" r="12"/><rect x="25" y="31" width="10" height="7"/><path d="M4 34 H28 V62 H4 Z"/><path d="M32 34 H56 V62 H32 Z"/></g><g stroke="var(--gold)" stroke-width="3"><line x1="30" y1="0" x2="30" y2="5"/><line x1="12" y1="8" x2="16" y2="12"/><line x1="48" y1="8" x2="44" y2="12"/></g><g stroke="#fff" stroke-width="2"><line x1="9" y1="44" x2="23" y2="44"/><line x1="37" y1="44" x2="51" y2="44"/><line x1="9" y1="52" x2="23" y2="52"/><line x1="37" y1="52" x2="51" y2="52"/></g></svg>
    <h3>BOAT TRAINING</h3><p>Hands-on instruction for new and experienced boaters.</p>
  </div>
  <div class="service abs" style="left:357px">
    <svg width="64" height="64" viewBox="0 0 64 64"><g fill="var(--gold)"><rect x="24" y="4" width="16" height="10"/><rect x="16" y="16" width="32" height="14"/><path d="M4 34 H60 L52 52 H12 Z"/><path d="M4 58 Q12 53 20 58 Q28 63 36 58 Q44 53 52 58 Q58 61 60 58 V62 H4 Z"/></g></svg>
    <h3>CHARTERS</h3><p>Relax and explore with captain-guided charters.</p>
  </div>
  <div class="service abs" style="left:612px">
    <svg width="76" height="64" viewBox="0 0 76 64"><g fill="var(--gold)"><path d="M6 8 Q22 2 36 10 V58 Q22 50 6 56 Z"/><path d="M70 8 Q54 2 40 10 V58 Q54 50 70 56 Z"/><path d="M2 14 V62 H74 V14 H72 V60 H4 V14 Z"/></g></svg>
    <h3>FIRST MATE SERIES</h3><p>Books to help you make informed decisions on and off the water.</p>
  </div>
  <div class="service abs" style="left:865px">
    <svg width="68" height="64" viewBox="0 0 68 64"><g fill="none" stroke="var(--gold)" stroke-width="3"><rect x="18" y="2" width="32" height="22"/><line x1="24" y1="10" x2="44" y2="10"/><line x1="24" y1="16" x2="44" y2="16"/><line x1="34" y1="24" x2="34" y2="34"/><rect x="14" y="34" width="40" height="8"/></g><g fill="var(--gold)"><circle cx="8" cy="34" r="5"/><circle cx="60" cy="34" r="5"/><rect x="3" y="42" width="10" height="20"/><rect x="55" y="42" width="10" height="20"/><rect x="30" y="42" width="8" height="20"/></g></svg>
    <h3>PRIVATE COACHING</h3><p>Personalized training for your goals.</p>
  </div>
  <a class="btn" href="#" style="left:142px;top:3228px;width:154px;height:47px">Learn More</a>
  <a class="btn" href="#" style="left:396px;top:3228px;width:154px;height:47px">View Charters</a>
  <a class="btn" href="#" style="left:650px;top:3228px;width:154px;height:47px">See the Books</a>
  <a class="btn" href="#" style="left:903px;top:3228px;width:154px;height:47px">Get Started</a>
</section>

<footer class="site-footer abs">
  <div class="abs" style="left:112px;top:65px;width:148px;height:148px;border-radius:50%;background:var(--white);display:flex;align-items:center;justify-content:center"><div class="brand-name" style="width:118px;font-size:14px">Captain Harlan's Boat Training &amp; Charters</div></div>
  <h4 style="left:331px">QUICK LINKS</h4>
  <div class="col abs" style="left:331px;top:105px"><a href="#">Home</a><a href="#">Services</a><a href="#">Boating Aids</a><a href="#">Gallery</a><a href="#">Contact</a><a href="#">Book A Charter</a></div>
  <h4 style="left:525px">CONTACT US</h4>
  <div class="col abs" style="left:525px;top:105px"><span>Marlow Cove, Florida</span><span>Mail: service@harlanboating.com</span><span>Tel: (555) 014-2290</span></div>
  <h4 style="left:813px">FOLLOW US</h4>
  <div class="social abs">
    <a href="#" aria-label="Email"><svg viewBox="0 0 18 18"><rect x="1" y="4" width="16" height="11" fill="none" stroke="#fff" stroke-width="1.8"/><path d="M1 4 L9 10 L17 4" fill="none" stroke="#fff" stroke-width="1.8"/></svg></a>
    <a href="#" aria-label="Share"><svg viewBox="0 0 18 18"><g fill="#fff"><circle cx="14" cy="3.5" r="2.5"/><circle cx="4" cy="9" r="2.5"/><circle cx="14" cy="14.5" r="2.5"/></g><path d="M14 3.5 L4 9 L14 14.5" fill="none" stroke="#fff" stroke-width="1.6"/></svg></a>
    <a href="#" aria-label="Message"><svg viewBox="0 0 18 18"><path d="M2 2 H16 V12 H7 L3 16 V12 H2 Z" fill="#fff"/></svg></a>
    <a href="#" aria-label="Website"><svg viewBox="0 0 18 18"><g fill="none" stroke="#fff" stroke-width="1.6"><circle cx="9" cy="9" r="7.5"/><ellipse cx="9" cy="9" rx="3.2" ry="7.5"/><line x1="1.5" y1="9" x2="16.5" y2="9"/></g></svg></a>
  </div>
  <p class="abs" style="left:813px;top:154px;width:290px;font-size:15px;line-height:26px;font-weight:500">© 2024 Captain Harlan’s Boat Training &amp; Charters, LLC. All rights reserved.</p>
</footer>

</body>
</html>
```